Alberta, Canada based Environmental Oilfield Consultant need a Business Card Design

We need a business card design for a year old company based in Edmonton, Alberta, Canada called Ferncrest Consulting Inc. We are environmental consultants primarily for oilfield based companies (pipeline cleanup, site consultations, environmental site training, and site evaluations).

We like the color blue or green, something very clean and crisp looking.
We don't really care if there is an otter on it but most of our work is land based and nothing really to do with oceans or larger bodies of water.

The name Ferncrest was the name of our fathers boat, and named our company that in his memory.

```html
<!DOCTYPE html>
<html lang="en">
<head>
<meta charset="utf-8">
<title>Ferncrest Consulting Inc. – Business Cards</title>
<link href="https://fonts.googleapis.com/css2?family=Questrial&display=swap" rel="stylesheet">
<style>
  :root {
    --page-bg: #e9ebe6;
    --card-white: #ffffff;
    --green-deep: #4f8a12;
    --green-mid: #7cb324;
    --green-light: #b7dc57;
    --green-pale: #dff0b4;
    --ink: #1d1f1a;
    --ink-soft: #3a3d36;
    --brand-green: #5e9a17;
  }
  * { box-sizing: border-box; margin: 0; padding: 0; }
  html, body {
    width: 1200px;
    height: 784px;
    overflow: hidden;
    background: var(--page-bg);
    font-family: "Questrial", "Century Gothic", sans-serif;
  }
  .sheet {
    position: relative;
    width: 1200px;
    height: 784px;
  }
  .card {
    position: absolute;
    top: 237px;
    width: 540px;
    height: 310px;
    border-radius: 4px;
    overflow: hidden;
    box-shadow: 0 6px 18px rgba(0,0,0,0.18);
  }
  .card--front { left: 40px; }
  .card--back { left: 620px; background: var(--card-white); }

  /* front */
  .front-pattern {
    position: absolute;
    inset: 0;
    background:
      radial-gradient(ellipse at 78% 40%, rgba(255,255,255,0.35) 0%, rgba(255,255,255,0) 55%),
      linear-gradient(135deg, var(--green-deep) 0%, var(--green-mid) 55%, var(--green-light) 100%);
  }
  .brand {
    position: absolute;
    display: flex;
    align-items: center;
    gap: 14px;
  }
  .brand__dot {
    width: 54px;
    height: 54px;
    border-radius: 50%;
    flex: none;
  }
  .brand__name {
    font-size: 30px;
    line-height: 1.05;
    letter-spacing: 3px;
    text-transform: uppercase;
  }
  .brand__name small {
    display: block;
    font-size: 15px;
    letter-spacing: 6px;
  }
  .card--front .brand { left: 52px; top: 104px; }
  .card--front .brand__dot { background: var(--green-pale); }
  .card--front .brand__name { color: var(--ink); }

  /* back */
  .card--back .brand { left: 36px; top: 44px; }
  .card--back .brand__dot { background: var(--green-mid); }
  .card--back .brand__name { color: var(--brand-green); }
  .swoosh {
    position: absolute;
    inset: 0;
    width: 100%;
    height: 100%;
  }
  .contact {
    position: absolute;
    left: 36px;
    top: 168px;
    color: var(--ink);
  }
  .contact__name {
    font-size: 19px;
    color: var(--brand-green);
    line-height: 1.1;
  }
  .contact__role {
    font-size: 13px;
    color: var(--ink-soft);
    margin-bottom: 14px;
  }
  .contact__list { list-style: none; }
  .contact__item {
    display: flex;
    align-items: center;
    gap: 7px;
    font-size: 15px;
    line-height: 21px;
  }
  .contact__icon { width: 14px; height: 14px; flex: none; }
</style>
</head>
<body>
<main class="sheet">

  <section class="card card--front" aria-label="Card front">
    <div class="front-pattern" role="img" aria-label="Green gradient background with a pattern of pale circles"></div>
    <div class="brand">
      <span class="brand__dot"></span>
      <p class="brand__name">Ferncrest<small>Consulting Inc.</small></p>
    </div>
  </section>

  <section class="card card--back" aria-label="Card back">
    <svg class="swoosh" viewBox="0 0 540 310" preserveAspectRatio="none" aria-hidden="true">
      <defs>
        <linearGradient id="swooshFill" x1="0" y1="1" x2="1" y2="0">
          <stop offset="0" stop-color="#7cb324"/>
          <stop offset="1" stop-color="#b7dc57"/>
        </linearGradient>
      </defs>
      <path d="M0,296 C170,286 360,230 540,140 L540,310 L0,310 Z" fill="#dff0b4"/>
      <path d="M0,302 C180,294 370,246 540,162 L540,310 L0,310 Z" fill="url(#swooshFill)"/>
    </svg>

    <div class="brand">
      <span class="brand__dot"></span>
      <p class="brand__name">Ferncrest<small>Consulting Inc.</small></p>
    </div>

    <div class="contact">
      <p class="contact__name">Dana Whitlock</p>
      <p class="contact__role">Director</p>
      <ul class="contact__list">
        <li class="contact__item">
          <svg class="contact__icon" viewBox="0 0 16 16" aria-hidden="true"><path d="M3 1.5l3 .5 1 3.5-2 1.2a9 9 0 0 0 4.3 4.3l1.2-2 3.5 1 .5 3c-1 1.5-3 1.8-5 .8A14 14 0 0 1 1.7 6.5C.8 4.5 1.5 2.5 3 1.5z" fill="#5e9a17"/></svg>
          0470 135 790
        </li>
        <li class="contact__item">
          <svg class="contact__icon" viewBox="0 0 16 16" aria-hidden="true"><rect x="1" y="3" width="14" height="10" rx="1" fill="#5e9a17"/><path d="M1.5 3.8L8 9l6.5-5.2" fill="none" stroke="#fff" stroke-width="1.3"/></svg>
          dana@ferncrestconsulting.com
        </li>
        <li class="contact__item">
          <svg class="contact__icon" viewBox="0 0 16 16" aria-hidden="true"><circle cx="8" cy="8" r="7" fill="#5e9a17"/><path d="M1 8h14M8 1c-3 3.5-3 10.5 0 14M8 1c3 3.5 3 10.5 0 14" fill="none" stroke="#fff" stroke-width="1"/></svg>
          www.ferncrestconsulting.com
        </li>
      </ul>
    </div>
  </section>

</main>
</body>
</html>
```